Zielgruppe
Wir entwickeln eine Software die die Vesmo Spracherkennung unter Windows ermöglicht. So kann die Spracherkennung in jeder beliebigen Software genutzt werden.
Aufgabenstellung
Die Software die die Webseite bewirbt nennt sich NoKeyPad. Logo befindet sich im Anhang. Achtung: Das logo sollte Weiß auf Blau, oder nur Blau sein. Die Webseite sollte sich ebenfalls im Blauton-bereich bewegen.
Wir möchten eine Webseite die mit viel Emotion und wenig Text arbeitet. Die Webseite soll hell, modern und frisch aussehen. Die webseite soll direkt auf der Startseite das Registrieren bzw Runterladen des Software ermöglichen. Genau wie es z.b. bei trelvo.com der Fall ist. Wir möchten viel mit Icons und kleineren lockeren Illustrationen arbeiten. Gerne auch Comic ähnliche Zeichnungen.
The software that advertises the website is called NoKeyPad. Logo can be found in the attachemnts. Attention: The logo should be white in blue, or only blue. The website should also be in the blue tone range.
We want a website that works with a lot of emotion and little text. The website should look bright, modern and fresh. The website should enable the registration or download of the software directly on the start page. Just like trelvo.com, for example. We want to work a lot with icons and smaller loose illustrations. Comic-like drawing are also welcome.

```html
<!DOCTYPE html>
<html lang="de">
<head>
<meta charset="utf-8">
<title>NoKeyPad – Vesmo Spracherkennung am Schreibtisch</title>
<link rel="stylesheet" href="https://fonts.googleapis.com/css2?family=Outfit:wght@300;400;500;600;700&display=swap">
<style>
  :root {
    --blue: #0a78d4;
    --ink: #262a3c;
    --text: #3b3f4e;
    --muted: #9a9da6;
    --bg-soft: #f6f6f6;
    --white: #ffffff;
    --footer: #272a3b;
    --line: #d8d9dd;
  }
  * { box-sizing: border-box; margin: 0; padding: 0; }
  html, body { width: 811px; height: 1200px; overflow: hidden; }
  body {
    position: relative;
    font-family: "Outfit", sans-serif;
    color: var(--text);
    background: var(--bg-soft);
  }
  .page-wave { position: absolute; left: 0; top: 0; width: 811px; height: 1200px; }

  /* Header */
  .site-header {
    position: absolute; left: 0; top: 0; width: 811px; height: 44px;
    background: var(--white);
  }
  .brand {
    position: absolute; left: 93px; top: 13px;
    display: flex; align-items: center; gap: 6px;
    font-size: 10.5px; font-weight: 600; color: var(--blue);
  }
  .brand-mark { width: 14px; height: 14px; background: var(--blue); border-radius: 3px; }
  .nav-link {
    position: absolute; top: 16px; font-size: 8.2px; color: var(--ink);
    text-decoration: none;
  }
  .nav-cta {
    position: absolute; left: 605px; top: 11px; width: 112px; height: 24px;
    border-radius: 12px; background: var(--blue); color: var(--white);
    font-size: 8.2px; font-weight: 600; display: flex; align-items: center; justify-content: center;
  }

  /* Hero */
  .hero-title {
    position: absolute; left: 93px; top: 100px; width: 400px;
    font-size: 27.5px; line-height: 30px; font-weight: 600; color: var(--ink);
    letter-spacing: -0.2px;
  }
  .hero-title .accent { color: var(--blue); }
  .hero-text {
    position: absolute; left: 93px; top: 206px; width: 370px;
    font-size: 9px; line-height: 14.3px; font-weight: 300; color: var(--text);
  }
  .signup-input {
    position: absolute; left: 93px; top: 289px; width: 163px; height: 31px;
    border: 1px solid var(--line); background: var(--white);
    font-family: inherit; font-size: 8.6px; font-style: italic; font-weight: 300;
    color: var(--muted); padding-left: 10px; display: flex; align-items: center;
  }
  .signup-button {
    position: absolute; left: 268px; top: 289px; width: 101px; height: 31px;
    border-radius: 16px; background: var(--blue); color: var(--white);
    font-size: 9.5px; font-weight: 600; display: flex; align-items: center; justify-content: center;
  }
  .hero-illustration {
    position: absolute; left: 506px; top: 91px; width: 282px; height: 302px;
    border-radius: 18px;
    background: linear-gradient(160deg, #e4e7ee 0%, #b9c9e4 45%, #3d4262 100%);
  }

  /* Sections */
  .section-title {
    position: absolute; left: 0; width: 811px; text-align: center;
    font-size: 27px; font-weight: 600; color: var(--ink);
  }
  .section-rule {
    position: absolute; left: 380px; width: 51px; height: 2.5px; background: var(--blue);
  }
  .card { position: absolute; width: 200px; text-align: center; }
  .card-icon { display: block; margin: 0 auto 12px; width: 36px; height: 36px; }
  .card-title {
    font-size: 11.5px; line-height: 13.5px; font-weight: 500; color: var(--blue);
    margin-bottom: 5px;
  }
  .card-text { font-size: 8.4px; line-height: 12.3px; font-weight: 300; color: var(--text); }

  /* Footer */
  .site-footer {
    position: absolute; left: 0; top: 1160px; width: 811px; height: 40px;
    background: var(--footer); color: var(--white); font-size: 7.4px;
  }
  .footer-copy { position: absolute; left: 93px; top: 15px; }
  .footer-links { position: absolute; right: 93px; top: 15px; display: flex; gap: 13px; }
</style>
</head>
<body>

<svg class="page-wave" viewBox="0 0 811 1200" aria-hidden="true">
  <path d="M0 506 C 160 460, 280 402, 405 402 C 540 402, 680 450, 811 495 L 811 740 C 680 790, 540 847, 405 847 C 280 847, 160 795, 0 751 Z" fill="#ffffff"/>
</svg>

<header class="site-header">
  <div class="brand"><span class="brand-mark"></span>NoKeyPad</div>
  <a class="nav-link" style="left:437px">Features</a>
  <a class="nav-link" style="left:502px">So funktioniert's</a>
  <div class="nav-cta">Jetzt ausprobieren</div>
</header>

<section class="hero">
  <h1 class="hero-title">Die bewerte Vesmo <span class="accent">Spracherkennung</span> auch am Schreibtisch nutzen</h1>
  <p class="hero-text">Lorem ipsum dolor sit amet, consetetur sadipscing elitr, sed diam nonumy eirmod tempor invidunt ut labore et dolore nonumy eirmod tempor invidunt ut labore et dolore magna aliquyam. Dolore nonumy eirmod tempor invidunt ut labore et dolore magna aliquyam.</p>
  <div class="signup-input">E-Mail-Adresse eintragen</div>
  <div class="signup-button">Download</div>
  <div class="hero-illustration" role="img" aria-label="Illustration: Frau sitzt auf einem Stuhl am Schreibtisch und arbeitet an einem blauen Laptop, daneben eine Topfpflanze"></div>
</section>

<section class="features">
  <h2 class="section-title" style="top:478px">Tool Features</h2>
  <div class="section-rule" style="top:515px"></div>

  <div class="card" style="left:91px; top:574px">
    <svg class="card-icon" viewBox="0 0 36 36" fill="none" stroke="#3b3f4e" stroke-width="1.1">
      <rect x="2" y="3" width="32" height="30" rx="2"/>
      <line x1="2" y1="9" x2="34" y2="9"/>
      <circle cx="5" cy="6" r="0.6" fill="#3b3f4e"/><circle cx="7.5" cy="6" r="0.6" fill="#3b3f4e"/><circle cx="10" cy="6" r="0.6" fill="#3b3f4e"/>
      <circle cx="18" cy="22" r="4"/>
      <path d="M18 14v2.5M18 27.5V30M10 22h2.5M23.5 22H26M12.4 16.4l1.8 1.8M21.8 25.8l1.8 1.8M12.4 27.6l1.8-1.8M21.8 18.2l1.8-1.8"/>
    </svg>
    <h3 class="card-title">Einfache Installation<br>als Browser Plugin</h3>
    <p class="card-text">Consetetur sadipscing elitr, sed diam nonumy eirmod tempor invidunt ut labore et dolore nonumy eirmod tempor invidunt ut labore et dolore magna aliquyam ...</p>
  </div>

  <div class="card" style="left:305px; top:574px">
    <svg class="card-icon" viewBox="0 0 36 36" fill="none" stroke="#3b3f4e" stroke-width="1.1">
      <path d="M4 4l3-1 10 10-2 2L5 5z"/>
      <path d="M17 17l12 12a2 2 0 0 1-3 3L14 20z"/>
      <path d="M30 4a5 5 0 0 0-6 6L6 28a2.5 2.5 0 1 0 3 3l18-18a5 5 0 0 0 6-6l-3 3-3-1-1-3z"/>
    </svg>
    <h3 class="card-title">Bewerte Technologie auch<br>am PC und Laptop nutzen</h3>
    <p class="card-text">Consetetur sadipscing elitr, sed diam nonumy eirmod tempor invidunt ut labore et dolore nonumy eirmod tempor invidunt ut labore et dolore magna aliquyam ...</p>
  </div>

  <div class="card" style="left:519px; top:574px">
    <svg class="card-icon" viewBox="0 0 36 36" fill="none" stroke="#3b3f4e" stroke-width="1.1">
      <circle cx="18" cy="18" r="14"/>
      <circle cx="18" cy="18" r="10"/>
      <path d="M18 18l5-5"/>
      <path d="M18 2v3M18 31v3M2 18h3M31 18h3M6.7 6.7l2 2M27.3 27.3l2 2M6.7 29.3l2-2M27.3 8.7l2-2"/>
      <circle cx="18" cy="18" r="1" fill="#3b3f4e"/>
    </svg>
    <h3 class="card-title">Zeitsparend für kurze Notizen,<br>E-Mails und lange Texte</h3>
    <p class="card-text">Consetetur sadipscing elitr, sed diam nonumy eirmod tempor invidunt ut labore et dolore nonumy eirmod tempor invidunt ut labore et dolore magna aliquyam ...</p>
  </div>
</section>

<section class="how-it-works">
  <h2 class="section-title" style="top:896px">So funktioniert's</h2>
  <div class="section-rule" style="top:932px"></div>

  <div class="card" style="left:91px; top:997px">
    <h3 class="card-title">Browser Plugin herrunterladen<br>und installieren</h3>
    <p class="card-text">Consetetur sadipscing elitr, sed diam nonumy eirmod tempor invidunt ut labore et dolore nonumy eirmod tempor invidunt ut labore et dolore magna aliquyam ...</p>
  </div>
  <div class="card" style="left:305px; top:997px">
    <h3 class="card-title">Kurze oder länger Passagen<br>aufnehmen</h3>
    <p class="card-text">Consetetur sadipscing elitr, sed diam nonumy eirmod tempor invidunt ut labore et dolore nonumy eirmod tempor invidunt ut labore et dolore magna aliquyam ...</p>
  </div>
  <div class="card" style="left:519px; top:997px">
    <h3 class="card-title">Aufzeichnung konvertieren und<br>als Textdatei speichern</h3>
    <p class="card-text">Consetetur sadipscing elitr, sed diam nonumy eirmod tempor invidunt ut labore et dolore nonumy eirmod tempor invidunt ut labore et dolore magna aliquyam ...</p>
  </div>
</section>

<footer class="site-footer">
  <div class="footer-copy">©2018 - NoKeyPad ist eine Marke der belvero Systemhaus GmbH. Alle Rechte vorbehalten.</div>
  <div class="footer-links"><span>Impressum</span><span>Bildnachweis</span><span>Datenschutz</span></div>
</footer>

</body>
</html>
```